Kelvard Engineers: Why you should hire us keepsake

New design. Open to plastic cards. We are an engineering firm that designs cell phone towers and commercial buildings. Please check out our website www.kelvardeng.example for more details. We want people to remember our card and for it to be useful if possible. We want the same look and feel on these cards to be translated to other marketing material we may need such as brochures.

Target Market(s)

Architects, Developers and Telecommunication Carriers

Industry/Entity Type

Engineering

Contact Information for Business Card

Card with our company colors, logo, and innovative design with elements related to our industry.

Font styles to use
Sans Serif

Colors
9bcb3c
abd036
0255a3

Requirements
Must have
• Sleek and hip design
Nice to have
• Bright lime green and navy coloring that pops with an innovative design.
Should not have
• A basic and boring design

```html
<!DOCTYPE html>
<html lang="en">
<head>
<meta charset="utf-8">
<title>Kelvard Engineers – Business Card</title>
<link href="https://fonts.googleapis.com/css2?family=Montserrat:wght@500;600;800&display=swap" rel="stylesheet">
<style>
  :root {
    --lime: #14ff1e;
    --navy: #0b2b5c;
    --navy-deep: #082552;
    --white: #ffffff;
    --backdrop: #e6e6e6;
  }
  html, body {
    margin: 0;
    padding: 0;
    width: 1200px;
    height: 1000px;
    overflow: hidden;
    background: var(--backdrop);
    font-family: "Montserrat", Arial, sans-serif;
  }
  .canvas { position: relative; width: 1200px; height: 1000px; }
  .card {
    position: absolute;
    left: 270px;
    width: 660px;
    height: 378px;
    border-radius: 18px;
    overflow: hidden;
    box-shadow: 0 4px 10px rgba(0,0,0,0.25);
  }
  .card-front { top: 108px; background: var(--lime); }
  .card-back { top: 522px; background: var(--navy); }

  .front-wordmark {
    position: absolute;
    left: 0; right: 0;
    top: 232px;
    transform: translateY(-50%);
    text-align: center;
    font-weight: 800;
    font-size: 96px;
    letter-spacing: -2px;
    color: var(--white);
    line-height: 1;
  }
  .city-band {
    position: absolute;
    left: 0; right: 0; bottom: 0;
    height: 40px;
    background: var(--navy);
    color: var(--white);
    font-size: 15px;
    font-weight: 500;
    letter-spacing: 0.5px;
    display: flex;
    align-items: center;
    justify-content: center;
    gap: 14px;
  }
  .city-band .sep { opacity: 0.9; }

  .back-wordmark {
    position: absolute;
    left: 50px;
    top: 172px;
    transform: translateY(-50%);
    font-weight: 800;
    font-size: 66px;
    letter-spacing: -1.5px;
    color: var(--lime);
    line-height: 1;
  }
  .divider {
    position: absolute;
    left: 330px;
    top: 140px;
    width: 1px;
    height: 115px;
    background: rgba(255,255,255,0.25);
  }
  .contact {
    position: absolute;
    left: 355px;
    top: 130px;
    color: var(--white);
  }
  .contact-name {
    margin: 0;
    font-size: 19px;
    font-weight: 600;
    color: var(--lime);
    line-height: 24px;
  }
  .contact-title {
    margin: 0 0 16px;
    font-size: 15px;
    font-weight: 500;
    line-height: 20px;
  }
  .contact-list { list-style: none; margin: 0; padding: 0; }
  .contact-list li {
    display: flex;
    align-items: center;
    gap: 6px;
    font-size: 15px;
    font-weight: 500;
    line-height: 21.5px;
  }
  .contact-list svg { width: 11px; height: 11px; fill: var(--lime); flex: none; }
  .tagline-band {
    position: absolute;
    left: 0; right: 0; bottom: 0;
    height: 39px;
    background: var(--lime);
    color: var(--white);
    font-size: 15px;
    font-weight: 500;
    display: flex;
    align-items: center;
    justify-content: center;
  }
</style>
</head>
<body>
<div class="canvas">
  <section class="card card-front">
    <div class="front-wordmark">Kelvard</div>
    <div class="city-band">
      <span>ATLANTA</span><span class="sep">|</span>
      <span>CHARLOTTE</span><span class="sep">|</span>
      <span>SAN ANTONIO</span><span class="sep">|</span>
      <span>HOUSTON</span>
    </div>
  </section>

  <section class="card card-back">
    <div class="back-wordmark">Kelvard</div>
    <div class="divider"></div>
    <div class="contact">
      <p class="contact-name">Dana Whitfield Morrow</p>
      <p class="contact-title">President</p>
      <ul class="contact-list">
        <li>
          <svg viewBox="0 0 12 12" aria-hidden="true"><path d="M2.4 0.6l2 2.2-1 1.4c.8 1.7 2 2.9 3.6 3.7l1.4-1 2.2 2-1.2 1.9C5.6 10.6 1.4 6.4.5 1.8z"/></svg>
          555.010.4821
        </li>
        <li>
          <svg viewBox="0 0 12 12" aria-hidden="true"><path d="M3 0h6a1 1 0 0 1 1 1v10a1 1 0 0 1-1 1H3a1 1 0 0 1-1-1V1a1 1 0 0 1 1-1zm.6 1.4v8h4.8v-8zM6 10a.6.6 0 1 0 0 1.2A.6.6 0 0 0 6 10z"/></svg>
          555.010.7390
        </li>
        <li>
          <svg viewBox="0 0 12 12" aria-hidden="true"><path d="M0 2h12v8H0zm1 .8L6 6.5l5-3.7V2.9z"/></svg>
          dmorrow@kelvardeng.example
        </li>
        <li>
          <svg viewBox="0 0 12 12" aria-hidden="true"><path d="M6 0a6 6 0 1 0 0 12A6 6 0 0 0 6 0zm0 1c.8.8 1.3 2.3 1.4 4.4H4.6C4.7 3.3 5.2 1.8 6 1zM1.1 6.6h2.5c.1 1.8.5 3.2 1.2 4.2A5 5 0 0 1 1.1 6.6zm0-1.2a5 5 0 0 1 3.7-4.2c-.7 1-1.1 2.4-1.2 4.2zm3.5 1.2h2.8C7.3 8.7 6.8 10.2 6 11c-.8-.8-1.3-2.3-1.4-4.4zm3.8 0h2.5a5 5 0 0 1-3.7 4.2c.7-1 1.1-2.4 1.2-4.2zm0-1.2c-.1-1.8-.5-3.2-1.2-4.2a5 5 0 0 1 3.7 4.2z"/></svg>
          www.kelvardeng.example
        </li>
      </ul>
    </div>
    <div class="tagline-band">Multi-discipline engineering</div>
  </section>
</div>
</body>
</html>
```